Logo & Visitenkarte für Consulting-Unternehmen
Der Designer ist von Beginn sehr gut auf meine Wünsche / Vorstellungen eingegangen und hat diese in sehr kurzer Zeit umgesetzt. Mein Logo bedarf kognitiver und emotionaler Intelligenz. Dadurch dass er das Logo im Kontext der Endvisualisierung (zB Visitenkarte) zeigte, machte für mich die Vorstellung des Ergebnisses sehr viel einfacher. Die Realisierung der Einzelschritte war sehr pragmatisch, schnell und angenehm.
Zielgruppe
Consulting, Begleitung, Inspiration, Beeinflussung
Prozessdesign
Aufgabenstellung
Verblüffend einfach, leicht und schnell zu verstehen.

```html
<!DOCTYPE html>
<html lang="de">
<head>
<meta charset="utf-8">
<title>Wandelwerk Beratung – Geschäftsausstattung</title>
<link rel="stylesheet" href="https://fonts.googleapis.com/css2?family=Source+Sans+3:ital,wght@0,400;0,600;0,700;1,400&display=swap">
<style>
  :root{
    --dark:#333333;
    --orange:#cc6600;
    --white:#ffffff;
    --stage:#a7a7a7;
    --top-light:#f4f4f4;
    --top-shade:#e2e2e2;
    --text:#2b2b2b;
  }
  *{box-sizing:border-box;margin:0;padding:0}
  html,body{width:892px;height:1200px;overflow:hidden}
  body{position:relative;font-family:"Source Sans 3",sans-serif;color:var(--text);background:var(--white)}
  .abs{position:absolute}

  /* brand lockup, scaled via font-size */
  .lockup{position:absolute;display:flex;flex-direction:column;align-items:center}
  .lockup-row{display:flex;align-items:center;gap:1.4em}
  .mark-dot{width:7.5em;height:7.5em;border-radius:50%;background:var(--orange);flex:none}
  .lockup-name{font-size:2.7em;font-weight:400;line-height:1.08;letter-spacing:.06em;text-transform:uppercase;color:var(--dark)}
  .lockup-rule{width:100%;height:1px;background:currentColor;margin:.9em 0 .5em;color:var(--dark)}
  .lockup-tag{font-size:1.85em;white-space:nowrap;color:var(--dark)}
  .lockup--light .lockup-name,.lockup--light .lockup-tag{color:var(--white)}
  .lockup--light .lockup-rule{color:var(--white)}
  .lockup--on-orange .mark-dot{background:var(--dark)}
  .lockup--on-orange .lockup-name,.lockup--on-orange .lockup-tag{color:var(--dark)}
  .lockup--on-orange .lockup-rule{color:var(--dark)}

  .hero{left:0;top:0;width:892px;height:226px;background:linear-gradient(var(--top-light),var(--top-shade))}
  .stage{left:0;top:226px;width:892px;height:744px;background:var(--stage)}

  /* letterhead */
  .letter{left:56px;top:272px;width:457px;height:647px;background:var(--white);font-size:8px;line-height:14px}
  .letter-edge{right:0;top:0;width:11px;height:100%;background:var(--dark)}
  .letter-rule{right:15px;top:0;width:1px;height:100%;background:var(--orange)}
  .sender-line{left:53px;top:104px;font-size:6px;text-decoration:underline;line-height:8px}
  .recipient{left:53px;top:123px;line-height:11px}
  .salutation{left:53px;top:232px}
  .body-copy{left:53px;top:260px;width:337px}
  .closing{left:53px;top:469px}
  .signature{left:53px;top:482px;width:90px;height:22px;background:linear-gradient(90deg,#e6e6e6,#d2d2d2)}
  .signer{left:53px;top:508px}
  .letter-foot{left:107px;top:593px;display:flex;font-size:5.5px;line-height:8.5px}
  .foot-col{padding:0 6px;border-left:1px solid var(--dark);height:54px}
  .foot-col:nth-child(1){width:116px}
  .foot-col:nth-child(2){width:82px}

  /* cards */
  .card{position:absolute;background:var(--white);overflow:hidden}
  .card-top{position:absolute;left:0;top:0;width:100%;background:var(--dark)}
  .card-rule{position:absolute;left:0;width:100%;height:2px;background:var(--orange)}
  .card-front{left:549px;top:270px;width:298px;height:194px}
  .card-person{left:55px;top:122px;font-size:10px;line-height:14px}
  .card-person b{font-weight:700}
  .card-address{left:157px;top:122px;font-size:10px;line-height:14px}
  .card-back{left:549px;top:496px;width:298px;height:193px}
  .card-web{left:0;top:146px;width:100%;text-align:center;font-size:11.5px;letter-spacing:.12em}
  .card-dark{left:549px;top:722px;width:301px;height:192px;background:var(--dark)}

  .panel-dark{left:0;top:972px;width:443px;height:228px;background:var(--dark)}
  .panel-orange{left:448px;top:972px;width:444px;height:228px;background:var(--orange)}
</style>
</head>
<body>

<section class="abs hero">
  <div class="lockup" style="left:256px;top:58px;width:350px;font-size:11px">
    <div class="lockup-row"><span class="mark-dot"></span><span class="lockup-name">Wandelwerk<br>Beratung</span></div>
    <div class="lockup-rule"></div>
    <div class="lockup-tag">Lena Krausfeld Consulting - Arbeitswelten 4.0</div>
  </div>
</section>

<section class="abs stage">
</section>

<article class="abs letter">
  <div class="abs letter-edge"></div>
  <div class="abs letter-rule"></div>
  <div class="lockup" style="left:271px;top:60px;width:155px;font-size:5px">
    <div class="lockup-row"><span class="mark-dot"></span><span class="lockup-name">Wandelwerk<br>Beratung</span></div>
    <div class="lockup-rule"></div>
    <div class="lockup-tag">Lena Krausfeld Consulting - Arbeitswelten 4.0</div>
  </div>
  <p class="abs sender-line">Ihre Firma GmbH, Friedrichstraße 21, 10179 Berlin</p>
  <p class="abs recipient">Firma Nordwerk GmbH<br>Hans Meier<br>Torstraße 78<br>10117 Berlin</p>
  <p class="abs salutation">Sehr geehrte Damen und Herren,</p>
  <p class="abs body-copy">Lorem ipsum dolor sit amet, consetetur sadipscing elitr, sed diam nonumy eirmod tempor invidunt ut labore et dolore magna aliquyam erat, sed diam voluptua. At vero eos et accusam et justo duo dolores et ea rebum. Stet clita kasd gubergren, no sea takimata sanctus est Lorem ipsum dolor sit amet. Lorem ipsum dolor sit amet, consetetur sadipscing elitr, sed diam nonumy eirmod tempor invidunt ut labore et dolore magna aliquyam erat, sed diam voluptua. At vero eos et accusam et justo duo dolores et ea rebum. Stet clita kasd gubergren, no sea takimata sanctus est Lorem ipsum dolor sit amet.<br>Lorem ipsum dolor sit amet, consetetur sadipscing elitr, sed diam nonumy eirmod tempor invidunt ut labore et dolore magna aliquyam erat, sed diam voluptua. At vero eos et accusam et justo duo dolores et ea rebum. Stet clita kasd gubergren, no sea takimata sanctus est Lorem ipsum dolor sit amet. Lorem ipsum dolor sit amet, consetetur sadipscing elitr, sed diam nonumy eirmod tempor invidunt ut labore et dolore magna aliquyam erat, sed diam voluptua. At vero eos et accusam et justo duo dolores et ea rebum. Stet clita kasd gubergren, no sea takimata sanctus est Lorem ipsum dolor sit amet.</p>
  <p class="abs closing">Mit freundlichen Grüßen</p>
  <div class="abs signature" role="img" aria-label="Handschriftliche Unterschrift"></div>
  <p class="abs signer">Bernd Hollmann</p>
  <div class="abs letter-foot">
    <div class="foot-col">Ihre Firma GmbH<br>Friedrichstr. 21<br>10179 Berlin<br>Telefon: +49(0)30 - 123 456 78<br>Fax: +49(0)30 - 123 456 79</div>
    <div class="foot-col">Geschäftsführer:<br>Bernd Hollmann<br><br>info@ihrefirma.de<br>www.ihrefirma.de</div>
    <div class="foot-col">Bankverbindung:<br>Ihre Bank AG - Berlin<br>IBAN: DE 01 2345 6789 3456 0123<br>BIC: FFXX DE XXXX<br>Ust.ID: 97865437</div>
  </div>
</article>

<article class="card card-front">
  <div class="card-top" style="height:97px"></div>
  <div class="card-rule" style="top:102px"></div>
  <div class="lockup lockup--light" style="left:55px;top:20px;width:190px;font-size:5.4px">
    <div class="lockup-row"><span class="mark-dot"></span><span class="lockup-name">Wandelwerk<br>Beratung</span></div>
    <div class="lockup-rule"></div>
    <div class="lockup-tag">Lena Krausfeld Consulting - Arbeitswelten 4.0</div>
  </div>
  <p class="abs card-person"><b>Lena Krausfeld</b><br><i>Unternehmerin</i></p>
  <p class="abs card-address">Lindenhofweg 7<br>8046 Zürich<br><span style="display:block;height:6px"></span>T: 079 000 12 34<br>lena-krausfeld@alpinnet.ch</p>
</article>

<article class="card card-back">
  <div class="card-top" style="height:97px"></div>
  <div class="card-rule" style="top:104px"></div>
  <div class="lockup lockup--light" style="left:0;top:26px;width:298px;font-size:5.4px">
    <div class="lockup-row"><span class="mark-dot"></span><span class="lockup-name">Wandelwerk<br>Beratung</span></div>
  </div>
  <p class="abs card-web">www.ihrefirma.de</p>
</article>

<article class="card card-dark">
  <div class="lockup lockup--light" style="left:0;top:68px;width:301px;font-size:7px">
    <div class="lockup-row"><span class="mark-dot"></span><span class="lockup-name">Wandelwerk<br>Beratung</span></div>
  </div>
</article>

<section class="abs panel-dark">
  <div class="lockup lockup--light" style="left:76px;top:56px;width:292px;font-size:9.2px">
    <div class="lockup-row"><span class="mark-dot"></span><span class="lockup-name">Wandelwerk<br>Beratung</span></div>
    <div class="lockup-rule"></div>
    <div class="lockup-tag">Lena Krausfeld Consulting - Arbeitswelten 4.0</div>
  </div>
</section>

<section class="abs panel-orange">
  <div class="lockup lockup--on-orange" style="left:91px;top:56px;width:292px;font-size:9.2px">
    <div class="lockup-row"><span class="mark-dot"></span><span class="lockup-name">Wandelwerk<br>Beratung</span></div>
    <div class="lockup-rule"></div>
    <div class="lockup-tag">Lena Krausfeld Consulting - Arbeitswelten 4.0</div>
  </div>
</section>

</body>
</html>
```